Trendora - Forex Signal Services Moment is All. Shape your path.

I need an attractive eye catching web design that is azure friendly. I currently have a web programmer working on the backend of my website. Now I need a professional design to attract and retain customers. This site needs to be mobile friendly.

Trendora is a highly reputable, trustworthy and professional site that offers forex signals to traders in all parts of the globe. With accurate and reliable forex signals, traders can not only make money but also boost their profits.

At Trendora, we want our clients to have complete faith on us and our services! We also do not want our users to lead a simple and monotonous life. Instead our goal is to help them create an extra source of steady income. However, this is possible only when our clients resolve to change their lives for the better. They need to change their mindset and most importantly develop a positive frame of mind. That’s exactly why at Trendora, we provide our clients with innumerable personal development tools and resources that’ll aid them in changing all the aspects of their lives. We want our traders to feel inspired and educate them in the right way!

Colors are flexible.

I do like the simplicity of www.bluemarrowtrade.example.
I do want a design more professional in appearance and not everything on page one.

I have not been able to decide on a logo. There is one of lower quality as I have not paid for it yet but I will if you decide it's the best for my business I will. Or should one feel that they have a better idea for a logo, I will pay for it if i like it.

I have included some of the content of my site so you can get a feel for where I am coming from.
(Please note that this content is still in the editing process)

Project Deadline Extended Reason: My content was not complete nor finalization of the final logo. We will allow a few more days for designers to modify the website.Thank you for your patience and understanding. Added Tuesday, January 24, 2017

Target Market(s)

I work with Forex Traders, Investors wanting to control their own portfolios, and remote nomads/mellienials

Coding

Coded - Design and coding required

Number of Pages Required

5+ page

Requirements
Must have
• I must have a professional clean look. I want the site to be interactive and eye catching. I want my audience hooked within seconds of opening it. It has to have all important information first. Photos must be legit and not spammy. I work as a representative in the financial market. I want my site to reflect that I stand by my product and reputation means everything to me. This site has to be engaging.
• Sorry, I should have included this earlier of what I will all need on this site.
• I'll have about Trendora (my company, what we stand for, who we work with, my strategy, etc....
• about me (why i started this company, who I am)
• Performance (graphs and recent posts of signals)
• Membership (how to sign up)
• Terms of service/legal/disclaimers
• FAQS
• Personal Development Resources
• Forex Education Resources
Nice to have
• Quick links to bounce around the site faster.
Should not have
• I do not want over the top white collar conservative.

```html
<!DOCTYPE html>
<html lang="en">
<head>
<meta charset="utf-8">
<title>Trendora - Forex Signal Services</title>
<link href="https://fonts.googleapis.com/css2?family=Fira+Sans+Condensed:wght@600;700&family=Open+Sans:wght@400;600;700&family=Fira+Sans:wght@300&display=swap" rel="stylesheet">
<style>
:root{
  --navy:#1f3a68;
  --navy-dark:#19325a;
  --ink:#222;
  --text:#333;
  --muted:#555;
  --card:#eeeeee;
  --pill:#a9a9a9;
  --footer:#2a2a2e;
  --white:#fff;
}
*{margin:0;padding:0;box-sizing:border-box}
html,body{width:1200px;height:2632px;overflow:hidden;background:var(--white)}
body{font-family:"Open Sans",sans-serif;color:var(--text);position:relative}
.heading{font-family:"Fira Sans Condensed",sans-serif;font-weight:700;text-transform:uppercase;text-align:center;color:var(--ink);font-size:27px;letter-spacing:-.2px}

/* header */
.site-nav{position:absolute;top:0;left:0;width:1200px;height:53px;background:var(--navy);z-index:2}
.brand{position:absolute;left:144px;top:7px;font-family:"Fira Sans",sans-serif;font-weight:300;font-size:31px;color:var(--white);letter-spacing:1px}
.menu{position:absolute;right:100px;top:18px;display:flex;gap:22px;list-style:none}
.menu li{font-weight:700;font-size:12.5px;color:var(--white);text-transform:uppercase}

/* hero */
.hero{position:absolute;top:0;left:0;width:1200px;height:561px;background:linear-gradient(120deg,#1c2430 0%,#4a5a6c 35%,#8fa0b2 55%,#3a4656 80%,#1a212b 100%)}
.hero-caption{position:absolute;left:207px;top:351px;width:330px;height:103px;background:rgba(15,20,30,.55);padding:6px 12px}
.hero-caption h1{font-family:"Open Sans",sans-serif;font-weight:600;font-size:44px;color:var(--white);line-height:1.1}
.hero-caption p{font-size:10px;color:var(--white);line-height:1.35;margin-top:4px}
.arrow{position:absolute;top:260px}
.arrow.left{left:12px}.arrow.right{right:12px}

/* welcome */
.welcome{position:absolute;top:600px;left:0;width:1200px}
.welcome .heading{margin-bottom:18px}
.welcome p{width:1030px;margin:0 auto;text-align:center;font-size:12px;line-height:22px;color:var(--text)}
.btn-primary{display:block;width:200px;height:40px;margin:25px auto 0;background:var(--navy);color:var(--white);font-weight:700;font-size:12px;text-transform:uppercase;text-align:center;line-height:40px;border-radius:2px}

/* services */
.services{position:absolute;top:874px;left:0;width:1200px;height:522px;background:var(--navy)}
.services .heading{color:var(--white);margin-top:52px}
.services .tagline{text-align:center;color:var(--white);font-size:12.5px;margin-top:8px}
.service-cards{position:absolute;top:138px;left:79px;display:flex;gap:27px}
.service-card{width:240px;height:344px;background:var(--card);border-radius:3px;text-align:center;padding-top:32px}
.icon-ring{width:50px;height:50px;border:2px solid var(--navy);border-radius:50%;margin:0 auto;display:flex;align-items:center;justify-content:center}
.service-card h3{font-family:"Open Sans",sans-serif;font-weight:700;font-size:17px;color:var(--ink);margin-top:22px}
.service-card p{font-size:12.5px;line-height:25px;color:var(--muted);width:200px;margin:14px auto 0;height:130px}
.btn-more{display:inline-flex;align-items:center;gap:6px;margin-top:16px;height:28px;padding:0 14px;border-radius:14px;background:var(--pill);color:var(--white);font-size:9px;font-weight:700;text-transform:uppercase}
.btn-more span.dot{width:13px;height:13px;border-radius:50%;background:var(--white);display:inline-flex;align-items:center;justify-content:center}

/* plans */
.plans{position:absolute;top:1450px;left:0;width:1200px}
.plan-grid{position:absolute;top:71px;left:79px;display:flex;gap:29px}
.plan{width:328px;height:338px;background:var(--navy);border-radius:3px;text-align:center;position:relative}
.plan h3{font-family:"Fira Sans Condensed",sans-serif;font-weight:700;font-size:20px;color:var(--white);padding-top:24px}
.plan .price{font-family:"Fira Sans Condensed",sans-serif;font-weight:700;font-size:21px;color:var(--white);margin-top:8px}
.plan .price small{font-size:12px;font-weight:600}
.plan-features{position:absolute;top:105px;left:7px;right:7px;height:146px;background:var(--white);list-style:none;padding-top:20px}
.plan-features::before{content:"";position:absolute;top:-1px;left:50%;margin-left:-13px;border-left:13px solid transparent;border-right:13px solid transparent;border-top:13px solid var(--navy)}
.plan-features li{font-size:11.5px;color:var(--muted);line-height:29px;display:flex;align-items:center;justify-content:center;gap:6px}
.plan .signup{position:absolute;top:264px;left:0;right:0;font-weight:700;font-size:12.5px;color:var(--white)}
.btn-order{position:absolute;top:298px;left:50%;margin-left:-51px;width:102px;height:30px;border-radius:15px;background:var(--white);color:var(--navy);font-size:10.5px;letter-spacing:.5px;text-transform:uppercase;line-height:30px}

/* faqs */
.faqs{position:absolute;top:1927px;left:0;width:1200px}
.faq-grid{position:absolute;top:71px;left:79px;display:grid;grid-template-columns:507px 507px;column-gap:26px;row-gap:19px}
.faq-item{height:40px;background:var(--navy);border-radius:2px;color:var(--white);font-size:16px;display:flex;align-items:center;padding-left:10px;gap:10px}
.faq-item .plus{font-size:13px;font-weight:700}

/* disclaimer */
.disclaimer{position:absolute;top:2310px;left:0;width:1200px}
.disclaimer .heading{margin-bottom:12px}
.disclaimer p{width:1040px;margin:0 auto;text-align:center;font-size:11.3px;line-height:21.5px;color:var(--text)}

/* footer */
.site-footer{position:absolute;top:2575px;left:0;width:1200px;height:57px;background:var(--footer)}
.site-footer p{position:absolute;left:79px;top:20px;font-size:11px;color:#888}
</style>
</head>
<body>

<header class="site-nav">
  <div class="brand">TRENDORA</div>
  <ul class="menu">
    <li>Home</li><li>About Us</li><li>Personal Development Resources</li><li>Forex Education Resources</li><li>FAQs</li><li>Contact Us</li>
  </ul>
</header>

<section class="hero" role="img" aria-label="Photo of glossy 3D bar and pie charts with rising stock figures">
  <svg class="arrow left" width="20" height="36" viewBox="0 0 20 36"><path d="M17 2 L3 18 L17 34" fill="none" stroke="#fff" stroke-width="3"/></svg>
  <svg class="arrow right" width="20" height="36" viewBox="0 0 20 36"><path d="M3 2 L17 18 L3 34" fill="none" stroke="#fff" stroke-width="3"/></svg>
  <div class="hero-caption">
    <h1>Lorem Ipsum</h1>
    <p>Lorem ipsum dolor sit amet, consetetur sadipscing elitr sed diam nonumy eirmod tempor invidunt ut labore et dolore magna aliquyam erat sed diam voluptua.</p>
  </div>
</section>

<section class="welcome">
  <h2 class="heading">Welcome to Trendora</h2>
  <p>Are you tired of incurring losses in the forex market? Do you find you are right correct in your trades but just at the wrong time? Do you need a reliable and efficient trading platform that allows you to earn profits consistently? We use proven strategies to help traders in succeeding in the forex market. Our forex experts provide high-probability, professional and consistent forex signals and charts that help traders in maximizing their profits and eliminating losses. Our Forex Signal Service aims to help you make money every month from the forex signals that we send you. Forex charts are analyzed daily. When a profitable entry point is identified, the signal is sent to our subscribers so they can make money.</p>
  <div class="btn-primary">Become a member today!</div>
</section>

<section class="services">
  <h2 class="heading">Forex Signal Services</h2>
  <p class="tagline">Moment is All. Shape your path.</p>
  <div class="service-cards">
    <article class="service-card">
      <div class="icon-ring"><svg width="26" height="22" viewBox="0 0 26 22" fill="#1f3a68"><circle cx="13" cy="6" r="4"/><path d="M6 20c0-5 3-8 7-8s7 3 7 8z"/><circle cx="5" cy="8" r="3"/><path d="M0 19c0-4 2-6 5-6 1 0 2 .3 2.6.8C5.8 15 5 17 5 19z"/><circle cx="21" cy="8" r="3"/><path d="M26 19c0-4-2-6-5-6-1 0-2 .3-2.6.8C20.2 15 21 17 21 19z"/></svg></div>
      <h3>Our Strategy</h3>
      <p>Trendora.com works with both day as well as intra-day traders. We only hold a maximum of one position at any given point in time. Once we've placed an order we do not move SL or TP targets.</p>
      <div class="btn-more">Read more <span class="dot"><svg width="7" height="7" viewBox="0 0 7 7"><path d="M2 1l3 2.5L2 6" fill="none" stroke="#a9a9a9" stroke-width="1.5"/></svg></span></div>
    </article>
    <article class="service-card">
      <div class="icon-ring"><svg width="20" height="26" viewBox="0 0 20 26"><text x="10" y="21" text-anchor="middle" font-family="Open Sans, sans-serif" font-weight="700" font-size="22" fill="#1f3a68">?</text></svg></div>
      <h3>Why Us?</h3>
      <p>Put simply, because we're different! We are a 'Never before Seen' forex trading company that is focused on guiding, mentoring and assisting traders in every possible manner.</p>
      <div class="btn-more">Read more <span class="dot"><svg width="7" height="7" viewBox="0 0 7 7"><path d="M2 1l3 2.5L2 6" fill="none" stroke="#a9a9a9" stroke-width="1.5"/></svg></span></div>
    </article>
    <article class="service-card">
      <div class="icon-ring"><svg width="24" height="22" viewBox="0 0 24 22" fill="none" stroke="#1f3a68" stroke-width="2"><rect x="1" y="1" width="22" height="20" rx="2"/><path d="M7 17V11M11 17V6M15 17V9M19 17V13" /></svg></div>
      <h3>Forex Traders</h3>
      <p>A forex signal service is provided for those who are struggling to make money on the forex market. We know that the forex market is ruthless and can cut you in so many ways.</p>
      <div class="btn-more">Read more <span class="dot"><svg width="7" height="7" viewBox="0 0 7 7"><path d="M2 1l3 2.5L2 6" fill="none" stroke="#a9a9a9" stroke-width="1.5"/></svg></span></div>
    </article>
    <article class="service-card">
      <div class="icon-ring"><svg width="24" height="24" viewBox="0 0 24 24" fill="none" stroke="#1f3a68" stroke-width="1.8" stroke-linejoin="round"><rect x="2" y="10" width="5" height="11"/><path d="M7 11l4-8c2 0 3 1 2.5 3.5L13 9h6c1.5 0 2.5 1.3 2 2.8l-2 7c-.3 1.2-1.2 2.2-2.5 2.2H7"/></svg></div>
      <h3>Investors And Retirees</h3>
      <p>If you are someone that has been tricked before or have lost your savings to investment companies and would like to know how you can take care of your own investment.</p>
      <div class="btn-more">Read more <span class="dot"><svg width="7" height="7" viewBox="0 0 7 7"><path d="M2 1l3 2.5L2 6" fill="none" stroke="#a9a9a9" stroke-width="1.5"/></svg></span></div>
    </article>
  </div>
</section>

<section class="plans">
  <h2 class="heading">Membership Plans</h2>
  <div class="plan-grid">
    <article class="plan">
      <h3>BASIC</h3>
      <div class="price">$60<small>/MONTH</small></div>
      <ul class="plan-features">
        <li><svg width="10" height="9" viewBox="0 0 10 9"><path d="M1 4.5l3 3L9 1" fill="none" stroke="#1f3a68" stroke-width="2"/></svg>Lorem ipsum dolor sit amet</li>
        <li><svg width="10" height="9" viewBox="0 0 10 9"><path d="M1 4.5l3 3L9 1" fill="none" stroke="#1f3a68" stroke-width="2"/></svg>Lorem ipsum dolor sit amet</li>
        <li><svg width="10" height="9" viewBox="0 0 10 9"><path d="M1 4.5l3 3L9 1" fill="none" stroke="#1f3a68" stroke-width="2"/></svg>Lorem ipsum dolor sit amet</li>
        <li><svg width="10" height="9" viewBox="0 0 10 9"><path d="M1 4.5l3 3L9 1" fill="none" stroke="#1f3a68" stroke-width="2"/></svg>Lorem ipsum dolor sit amet</li>
      </ul>
      <div class="signup">Click here to sign up for 1 month</div>
      <div class="btn-order">Order now</div>
    </article>
    <article class="plan">
      <h3>ADVANCED</h3>
      <div class="price">$150<small>/MONTH</small></div>
      <ul class="plan-features">
        <li><svg width="10" height="9" viewBox="0 0 10 9"><path d="M1 4.5l3 3L9 1" fill="none" stroke="#1f3a68" stroke-width="2"/></svg>Lorem ipsum dolor sit amet</li>
        <li><svg width="10" height="9" viewBox="0 0 10 9"><path d="M1 4.5l3 3L9 1" fill="none" stroke="#1f3a68" stroke-width="2"/></svg>Lorem ipsum dolor sit amet</li>
        <li><svg width="10" height="9" viewBox="0 0 10 9"><path d="M1 4.5l3 3L9 1" fill="none" stroke="#1f3a68" stroke-width="2"/></svg>Lorem ipsum dolor sit amet</li>
        <li><svg width="10" height="9" viewBox="0 0 10 9"><path d="M1 4.5l3 3L9 1" fill="none" stroke="#1f3a68" stroke-width="2"/></svg>Lorem ipsum dolor sit amet</li>
      </ul>
      <div class="signup">Click here to sign up for 3 months</div>
      <div class="btn-order">Order now</div>
    </article>
    <article class="plan">
      <h3>PROFESSIONAL</h3>
      <div class="price">$600<small>/MONTH</small></div>
      <ul class="plan-features">
        <li><svg width="10" height="9" viewBox="0 0 10 9"><path d="M1 4.5l3 3L9 1" fill="none" stroke="#1f3a68" stroke-width="2"/></svg>Lorem ipsum dolor sit amet</li>
        <li><svg width="10" height="9" viewBox="0 0 10 9"><path d="M1 4.5l3 3L9 1" fill="none" stroke="#1f3a68" stroke-width="2"/></svg>Lorem ipsum dolor sit amet</li>
        <li><svg width="10" height="9" viewBox="0 0 10 9"><path d="M1 4.5l3 3L9 1" fill="none" stroke="#1f3a68" stroke-width="2"/></svg>Lorem ipsum dolor sit amet</li>
        <li><svg width="10" height="9" viewBox="0 0 10 9"><path d="M1 4.5l3 3L9 1" fill="none" stroke="#1f3a68" stroke-width="2"/></svg>Lorem ipsum dolor sit amet</li>
      </ul>
      <div class="signup">Click here to sign up for 12 months</div>
      <div class="btn-order">Order now</div>
    </article>
  </div>
</section>

<section class="faqs">
  <h2 class="heading">FAQs</h2>
  <div class="faq-grid">
    <div class="faq-item"><span class="plus">+</span>Why Trendora?</div>
    <div class="faq-item"><span class="plus">+</span>What Is Your Trading Philosophy And Style?</div>
    <div class="faq-item"><span class="plus">+</span>How Many Signals Do You Send A Month?</div>
    <div class="faq-item"><span class="plus">+</span>How Many Pips Can I Make Per Month?</div>
    <div class="faq-item"><span class="plus">+</span>Can I Follow Your Signals And Have A Full Time Job?</div>
    <div class="faq-item"><span class="plus">+</span>How Will I Receive My Signals?</div>
    <div class="faq-item"><span class="plus">+</span>How Do I Subscribe To Your Service?</div>
    <div class="faq-item"><span class="plus">+</span>What Happens After My Trial Period Access?</div>
    <div class="faq-item"><span class="plus">+</span>How Will Forex Signals Help You?</div>
    <div class="faq-item"><span class="plus">+</span>What We Do For You?</div>
  </div>
</section>

<section class="disclaimer">
  <h2 class="heading">Disclaimer</h2>
  <p>Disclaimer Trading foreign exchange ("Forex") on margin carries a high level of risk, and may not be suitable for all investors. Before deciding to trade Forex you should carefully consider your investment objectives, level of experience, and only trade with the money you are prepared to lose. The possibility exists that you could sustain a loss in excess of all of your deposited funds and therefore you should not speculate with capital that you cannot afford to lose. You should be aware of all the risks associated with foreign exchange. Clients must be at least 18 years old to use the services of TRENDORA. You acknowledge that past performance is not an indicator of future returns and that references to performance on this Site are provided as historical benchmarks only. TRENDORA does not take responsibility for loss incurred as a result of our trading signals. By signing up as a member you acknowledge that we are not providing financial advice and that you are making the decision to use our trades on your own account. All information provided by TRENDORA, in any form, is for educational purposes only.</p>
</section>

<footer class="site-footer">
  <p>© Trendora, 2017. All Rights Reserved.</p>
</footer>

</body>
</html>
```